Black Matte card with samurai logo which I would like it to be textured and company name on one side and on the other side I would like the company information with the kaze (Face logo) Sushi logo. Double Sided card.

Target Market(s)

majority customers are University students, University sororities and fraternities.

Industry/Entity Type

It Company

Contact Information for Business Card

Kaze Grill
317 W. Marlow Rd
Tucson, AZ 85702
Phone (520)555-0147
Fax (520)555-0193
E-mail: Kazegrillaz@mailpost.example
FB: Kazegrillaz
Twitter: Kazegrillaz

Font styles to use
Other font styles liked:
• Present Normal

```html
<!DOCTYPE html>
<html lang="en">
<head>
<meta charset="utf-8">
<title>Kaze Grill — Business Card</title>
<link rel="stylesheet" href="https://fonts.googleapis.com/css2?family=Kurale&family=PT+Sans:wght@400&display=swap">
<style>
  :root {
    --page-bg: #ece9e4;
    --card-black: #1d1c1d;
    --slat-light: #3a3a3b;
    --slat-dark: #111112;
    --brand-red: #b3302a;
    --ink: #2a2a2a;
    --paper: #ffffff;
    --name-font: "Kurale", serif;
    --info-font: "PT Sans", sans-serif;
  }
  * { margin: 0; padding: 0; box-sizing: border-box; }
  html, body { width: 1200px; height: 1172px; overflow: hidden; }
  body { background: var(--page-bg); position: relative; }

  .card { position: absolute; width: 911px; height: 519px; overflow: hidden; }

  /* Front side */
  .card-front { left: 40px; top: 37px; background: var(--card-black); }
  .front-texture {
    position: absolute; inset: 0;
    background: linear-gradient(180deg, var(--slat-light) 0%, var(--slat-dark) 55%, var(--slat-light) 100%);
  }
  .front-mark {
    position: absolute; left: 344px; top: 100px;
    width: 220px; height: 220px; border-radius: 50%;
    background: var(--brand-red);
  }
  .front-name {
    position: absolute; left: 0; right: 0; top: 382px;
    text-align: center;
    font-family: var(--name-font); font-size: 76px; line-height: 1;
    color: var(--brand-red);
  }

  /* Back side */
  .card-back { left: 257px; top: 609px; background: var(--paper); box-shadow: 0 0 0 1px #d8d5d0; }
  .back-wave { position: absolute; inset: 0; }
  .back-mark {
    position: absolute; left: 156px; top: 70px;
    width: 140px; height: 140px; border-radius: 50%;
    background: var(--brand-red);
  }
  .back-name {
    position: absolute; left: 96px; width: 260px; top: 238px;
    text-align: center; font-family: var(--name-font);
    color: var(--brand-red); line-height: 1;
  }
  .back-name .name-main { display: block; font-size: 76px; }
  .back-name .name-sub { display: block; font-size: 36px; margin-top: 4px; }

  .address {
    position: absolute; right: 21px; top: 74px;
    text-align: right; font-family: var(--info-font);
    font-size: 22px; line-height: 32px; color: var(--ink);
  }
  .contact-list {
    position: absolute; right: 21px; top: 344px;
    list-style: none; text-align: right;
    font-family: var(--info-font); font-size: 22px; line-height: 35px;
    color: var(--paper);
  }
  .contact-list li { display: flex; justify-content: flex-end; align-items: center; gap: 8px; }
  .contact-icon { width: 20px; height: 20px; flex: none; }
  .social-square { width: 20px; height: 20px; background: #5e7fb0; flex: none; }
</style>
</head>
<body>

<section class="card card-front" aria-label="Front of card">
  <div class="front-texture" role="img" aria-label="Dark brushed wood slat texture"></div>
  <div class="front-mark"></div>
  <p class="front-name">kaze grill</p>
</section>

<section class="card card-back" aria-label="Back of card">
  <svg class="back-wave" viewBox="0 0 911 519" width="911" height="519" aria-hidden="true">
    <path d="M0 412 C 210 500 430 510 610 390 C 730 310 830 250 911 238 L911 519 L0 519 Z" fill="var(--card-black)"/>
    <path d="M0 380 C 210 470 430 480 610 360 C 730 280 830 222 911 205" fill="none" stroke="var(--brand-red)" stroke-width="14"/>
    <path d="M0 400 C 200 480 420 488 600 372 C 720 294 830 236 911 222" fill="none" stroke="var(--paper)" stroke-width="4"/>
    <path d="M60 440 C 240 505 440 500 620 400" fill="none" stroke="var(--brand-red)" stroke-width="8"/>
  </svg>

  <div class="back-mark"></div>
  <p class="back-name"><span class="name-main">kaze</span><span class="name-sub">grill</span></p>

  <address class="address">
    Kaze Grill 317<br>
    W. Marlow Rd Tucson<br>
    AZ 85702
  </address>

  <ul class="contact-list">
    <li>
      <svg class="contact-icon" viewBox="0 0 20 20"><circle cx="10" cy="10" r="8.5" fill="none" stroke="#fff" stroke-width="1.5"/><path d="M7 5 L9 7 L8 9 Q9.5 11.5 11 12 L13 11 L15 13 L13 15 Q8 14 5 7 Z" fill="#fff"/></svg>
      <span>(520)555-0147</span>
    </li>
    <li>
      <svg class="contact-icon" viewBox="0 0 20 20"><rect x="5.5" y="1.5" width="9" height="17" rx="1.5" fill="none" stroke="#fff" stroke-width="1.5"/><rect x="7.5" y="4" width="5" height="5" fill="#fff"/><path d="M7.5 11h5M7.5 13h5M7.5 15h5" stroke="#fff" stroke-width="1"/></svg>
      <span>(520)555-0193</span>
    </li>
    <li><span class="social-square"></span><span>Kazegrillaz</span></li>
    <li><span class="social-square"></span><span>Kazegrillaz</span></li>
    <li>
      <svg class="contact-icon" viewBox="0 0 20 20"><path d="M2 8 L10 3 L18 8 V16 H2 Z" fill="#fff"/><path d="M2 8 L10 13 L18 8" fill="none" stroke="#1d1c1d" stroke-width="1.3"/></svg>
      <span>Kazegrillaz@mailpost.example</span>
    </li>
  </ul>
</section>

</body>
</html>
```